Ductless Mini Split Business Website

Amber Kite Services is looking to design an eye catching educational website about installing Ductless mini splits.

Similar to this company.
https://www.cedarcoolair.com/

```html
<!DOCTYPE html>
<html lang="en">
<head>
<meta charset="utf-8">
<title>Amber Kite Services — Ductless Experts</title>
<link href="https://fonts.googleapis.com/css2?family=Prata&family=Poppins:ital,wght@0,400;0,500;0,600;0,700;1,400&display=swap" rel="stylesheet">
<style>
:root{
  --yellow:#ffcc00;
  --black:#000;
  --ink:#111;
  --text:#555;
  --muted:#888;
  --white:#fff;
  --line:#e5e5e5;
}
*{box-sizing:border-box;margin:0;padding:0}
html,body{width:1200px;height:4303px;overflow:hidden}
body{position:relative;background:var(--white);font-family:'Poppins',sans-serif;color:var(--ink)}
.abs{position:absolute}
.serif{font-family:'Prata',serif;font-weight:400}
.btn{position:absolute;display:flex;align-items:center;justify-content:center;border-radius:30px;font-size:12px;font-weight:600;letter-spacing:.3px;text-transform:uppercase}
.btn-dark{background:var(--ink);color:var(--white)}
.btn-yellow{background:var(--yellow);color:var(--ink);box-shadow:0 8px 18px rgba(255,204,0,.35)}
.photo{position:absolute}

/* header */
.brand{position:absolute;display:flex;align-items:center;gap:10px;font-weight:700;font-size:22px;color:var(--ink)}
.brand .dot{width:26px;height:26px;border-radius:50%;background:var(--yellow)}
.tagline{left:625px;top:50px;font-size:13px;font-weight:500}
.call-icon{left:893px;top:33px;width:48px;height:48px;border-radius:50%;background:var(--yellow);display:flex;align-items:center;justify-content:center}
.call-label{left:950px;top:40px;font-size:11px;font-weight:500}
.call-number{left:950px;top:52px;font-size:23px;font-weight:600}
.nav{left:0;top:114px;width:1200px;height:52px;background:var(--black);display:flex;align-items:center;padding-left:89px;gap:0}
.nav a{color:var(--white);font-size:13px;font-weight:500;text-decoration:none;padding:0 24px;border-right:1px solid #333;line-height:14px}
.nav a:first-child{color:var(--yellow);padding-left:0;position:relative}
.nav a:first-child::before{content:"";position:absolute;left:10px;top:-10px;width:4px;height:4px;border-radius:50%;background:var(--yellow)}
.nav a:last-child{border:none}

/* hero */
.hero-circle{left:90px;top:336px;width:488px;height:488px;border-radius:50%;background:var(--yellow);text-align:center}
.hero-title{position:absolute;left:0;right:0;top:128px;font-size:78px;line-height:1;letter-spacing:-1px}
.hero-sub{position:absolute;left:0;right:0;top:206px;font-size:36px}
.hero-rule{position:absolute;left:140px;top:260px;width:210px;height:1px;background:#c9a100}
.hero-lead{position:absolute;left:0;right:0;top:284px;font-size:19px}
.dots{display:flex;flex-direction:column;gap:9px}
.dots span{width:9px;height:9px;border-radius:50%;border:1px solid #999}
.dots span.on{border:2px solid var(--ink)}

/* about */
.eyebrow{font-size:11px;font-weight:600;color:var(--yellow);text-transform:uppercase}
.about-title{left:89px;top:1012px;font-size:37px}
.about-sub{left:89px;top:1057px;font-size:16px}
.about-rule{left:89px;top:1097px;width:48px;height:2px;background:var(--line)}
.about-copy{left:89px;width:420px;font-size:13.5px;line-height:24px;color:var(--text)}
.play{left:542px;top:1103px;width:108px;height:108px;border-radius:50%;background:var(--yellow);display:flex;align-items:center;justify-content:center}

/* services */
.section-title{left:0;width:1200px;text-align:center;font-size:36px}
.service{position:absolute;top:1567px;width:246px;height:321px}
.service span{position:absolute;left:0;right:0;bottom:14px;text-align:center;color:var(--white);font-size:14px;font-weight:600;line-height:16px;text-transform:uppercase}

/* why / contact */
.why{left:0;top:2164px;width:762px;height:555px;background:var(--black)}
.why-title{left:90px;top:2258px;font-size:36px;line-height:36px;color:var(--white)}
.why-item{position:absolute;left:90px;width:440px}
.why-item h4{margin-left:66px;color:var(--yellow);font-size:15px;font-weight:600;text-transform:uppercase}
.why-item p{margin-left:66px;margin-top:4px;color:#ddd;font-size:13px;line-height:18px}
.why-item svg{position:absolute;left:0;top:0}
.contact{left:597px;top:2092px;width:603px;height:555px;background:var(--yellow)}
.contact-title{left:642px;top:2167px;font-size:34px}
.field{position:absolute;background:var(--white);font-size:11.5px;font-weight:600;padding:0 12px;display:flex;align-items:center;text-transform:uppercase}
.field.select{font-weight:400;text-transform:none;color:#666;justify-content:space-between}
.field.area{align-items:flex-start;padding-top:16px}

/* reviews */
.avatar{position:absolute;border-radius:50%;background:linear-gradient(135deg,#d9c8b8,#8a8f98);border:3px solid var(--white);box-shadow:0 3px 8px rgba(0,0,0,.15)}
.quote{left:230px;top:3018px;width:740px;text-align:center;font-style:italic;font-size:16px;line-height:27px;color:#333}
.qmark{font-family:'Prata',serif;font-size:90px;color:#ddd;line-height:1}
.reviewer{left:0;width:1200px;text-align:center;top:3094px;font-size:12px;font-weight:600;color:var(--yellow);text-transform:uppercase}

/* promise */
.promise{position:absolute;top:3337px;width:325px;height:379px;background:var(--white);box-shadow:0 10px 30px rgba(0,0,0,.08)}
.promise .photo{left:0;top:0;width:325px;height:234px}
.promise h3{position:absolute;top:272px;left:0;right:0;text-align:center;font-size:21px;font-weight:500;letter-spacing:.5px}
.promise .btn{left:100px;top:316px;width:125px;height:36px;font-size:11px}

/* footer */
.footer-head{position:absolute;top:3962px;color:var(--yellow);font-size:15px;font-weight:500;text-transform:uppercase}
.footer-list{position:absolute;list-style:none;color:var(--white);font-size:13px}
.footer-list li{height:31px}
.footer-contact{position:absolute;color:var(--white);font-size:13px;line-height:22px}
.social{position:absolute;width:32px;height:32px;border-radius:50%}
.copyright{left:0;width:1200px;text-align:center;top:4267px;color:var(--white);font-size:12px}
</style>
</head>
<body>

<!-- header -->
<div class="brand" style="left:89px;top:42px"><span class="dot"></span>Amber Kite Services</div>
<div class="abs tagline">YOUR DUCTLESS SYSTEM EXPERTS</div>
<div class="abs call-icon">
  <svg width="22" height="22" viewBox="0 0 24 24"><path d="M6.6 10.8a15 15 0 0 0 6.6 6.6l2.2-2.2a1 1 0 0 1 1-.25 11.4 11.4 0 0 0 3.6.6 1 1 0 0 1 1 1V20a1 1 0 0 1-1 1A17 17 0 0 1 3 4a1 1 0 0 1 1-1h3.5a1 1 0 0 1 1 1c0 1.25.2 2.45.6 3.6a1 1 0 0 1-.25 1z" fill="#111"/></svg>
</div>
<div class="abs call-label">CALL US TODAY</div>
<div class="abs call-number">123-456-7890</div>
<nav class="abs nav">
  <a>HOME</a><a>ABOUT US</a><a>DUCTLESS HEAT PUMPS</a><a>DUCTLESS HEAT PUMPS FAQ</a><a>FINANCING</a><a>CUSTOMER REVIEWS</a><a>CONTACT US</a>
</nav>

<!-- hero -->
<svg class="abs" style="left:0;top:166px" width="1200" height="660" role="img" aria-label="Photo of a woman pointing a remote at a wall-mounted ductless unit in a bright room">
  <defs><linearGradient id="heroG" x1="0" y1="0" x2="1" y2="0"><stop offset="0" stop-color="#e9ecef"/><stop offset=".6" stop-color="#f4f5f6"/><stop offset="1" stop-color="#d8dde2"/></linearGradient></defs>
  <polygon points="0,0 1200,0 1200,540 0,655" fill="url(#heroG)"/>
</svg>
<div class="abs dots" style="left:1152px;top:416px"><span class="on"></span><span></span><span></span></div>
<div class="abs hero-circle">
  <div class="serif hero-title" style="font-weight:700">DUCTLESS</div>
  <div class="serif hero-sub">DOES IT BETTER</div>
  <div class="hero-rule"></div>
  <div class="hero-lead">Let Ductless Experts Show You How</div>
  <div class="btn btn-dark" style="left:143px;top:338px;width:204px;height:52px">Get in touch with us</div>
</div>

<!-- about -->
<div class="abs eyebrow" style="left:89px;top:992px">About us</div>
<div class="abs serif about-title">AMBER KITE SERVICES</div>
<div class="abs about-sub">Helping Portland &amp; Surrounding Areas Go Ductless</div>
<div class="abs about-rule"></div>
<p class="abs about-copy" style="top:1112px">Aenean sollicitudin, lorem quis bibendum auctor, nisi elit quat ipsum, nec sagittis sem nibh id elit. Duis sed odio sit amet nibh vulputate cursus a sit amet mauris.</p>
<p class="abs about-copy" style="top:1196px">Class aptent taciti sociosqu ad litora torquent per conubia nostra, per inceptos himenaeos. Mauris in erat justo. Nullam ac urna eu felis dapibus condimentum sit</p>
<div class="photo" role="img" aria-label="Photo of a technician servicing a wall-mounted ductless unit" style="left:595px;top:867px;width:515px;height:532px;background:linear-gradient(160deg,#f2f3f4,#c9ccd0 70%,#8b7a66);box-shadow:0 20px 40px rgba(0,0,0,.15)"></div>
<div class="abs play"><svg width="22" height="24" viewBox="0 0 22 24"><polygon points="4,2 20,12 4,22" fill="#111"/></svg></div>

<!-- services -->
<h2 class="abs serif section-title" style="top:1505px">HOW CAN WE HELP YOU?</h2>
<div class="service" role="img" aria-label="Photo of a technician cleaning a ductless unit" style="left:89px;background:linear-gradient(180deg,#9aa3ad,#2b3440)"><span>Ductless<br>Maintenance</span></div>
<div class="service" role="img" aria-label="Photo of a technician repairing a ceiling unit" style="left:347px;background:linear-gradient(180deg,#8f9499,#3b3f44)"><span>Ductless<br>Repairs</span></div>
<div class="service" role="img" aria-label="Photo of a hand holding a remote control" style="left:605px;background:linear-gradient(180deg,#e5e7e9,#8c9197)"><span>Ductless<br>Warranty</span></div>
<div class="service" role="img" aria-label="Photo of a smiling installer mounting a unit" style="left:864px;background:linear-gradient(180deg,#c4c6c8,#8a5a3c)"><span>Ductless<br>Installation</span></div>
<div class="btn btn-yellow" style="left:490px;top:1928px;width:220px;height:48px;font-size:11.5px">More ductless services</div>

<!-- why / contact -->
<div class="abs why"></div>
<div class="abs serif why-title">WHY CHOOSE<br>AMBER KITE SERVICES</div>
<div class="why-item" style="top:2372px">
  <svg width="44" height="56" viewBox="0 0 44 56" fill="none" stroke="#ffcc00" stroke-width="2"><rect x="4" y="4" width="30" height="44" rx="2"/><line x1="10" y1="16" x2="28" y2="16"/><line x1="10" y1="24" x2="28" y2="24"/><line x1="10" y1="32" x2="22" y2="32"/></svg>
  <h4>0% Financing for 60 months</h4>
  <p>Class aptent taciti sociosqu ad litora torquent per conubia nostra, per inceptos</p>
</div>
<div class="why-item" style="top:2463px">
  <svg width="44" height="56" viewBox="0 0 44 56" fill="none" stroke="#ffcc00" stroke-width="2"><path d="M4 24a18 18 0 0 1 36 0z"/><line x1="22" y1="24" x2="22" y2="44"/></svg>
  <h4>365 Day, money back guarantee</h4>
  <p>Class aptent taciti sociosqu ad litora torquent per conubia nostra, per inceptos</p>
</div>
<div class="why-item" style="top:2554px">
  <svg width="44" height="56" viewBox="0 0 44 56" fill="none" stroke="#ffcc00" stroke-width="2"><circle cx="22" cy="18" r="10"/><path d="M4 50a18 14 0 0 1 36 0"/></svg>
  <h4>We are the experts in ductless services</h4>
  <p>Class aptent taciti sociosqu ad litora torquent per conubia nostra, per inceptos</p>
</div>

<div class="abs contact"></div>
<h2 class="abs serif contact-title">CONTACT US TODAY</h2>
<div class="field" style="left:643px;top:2227px;width:231px;height:42px">First name*</div>
<div class="field" style="left:881px;top:2227px;width:229px;height:42px">Last name*</div>
<div class="field" style="left:643px;top:2281px;width:231px;height:42px">Email*</div>
<div class="field" style="left:881px;top:2281px;width:229px;height:42px">Phone*</div>
<div class="field select" style="left:643px;top:2334px;width:467px;height:42px"><span>Are you a new customer</span><span>⌄</span></div>
<div class="field area" style="left:643px;top:2387px;width:467px;height:104px">Message*</div>
<div class="btn btn-dark" style="left:643px;top:2515px;width:221px;height:50px;font-size:11.5px">More ductless services</div>

<!-- reviews -->
<h2 class="abs serif section-title" style="top:2812px">CLIENT REVIEWS</h2>
<div class="avatar" style="left:414px;top:2901px;width:48px;height:48px"></div>
<div class="avatar" style="left:487px;top:2901px;width:48px;height:48px"></div>
<div class="avatar" style="left:555px;top:2877px;width:88px;height:88px"></div>
<div class="avatar" style="left:664px;top:2901px;width:48px;height:48px"></div>
<div class="avatar" style="left:738px;top:2901px;width:48px;height:48px"></div>
<div class="abs" style="left:0;width:1200px;text-align:center;top:2985px;color:var(--yellow);font-size:18px;letter-spacing:2px">★★★★★</div>
<div class="abs qmark" style="left:170px;top:2990px">“</div>
<div class="abs qmark" style="left:808px;top:3050px">”</div>
<p class="abs quote">Aenean sollicitudin, lorem quis bibendum auctor, nisi elit consequat ipsum, nec sagittis sem nibh id elit. Duis sed odio sit amet nibh vulputate</p>
<div class="abs reviewer">Mara Lindqvist</div>
<div class="abs dots" style="left:1105px;top:2986px"><span class="on" style="width:11px;height:11px"></span><span></span><span></span></div>
<div class="abs" style="left:89px;top:3193px;width:1021px;height:1px;background:var(--line)"></div>

<!-- promise -->
<h2 class="abs serif section-title" style="top:3275px">WE STAND BEHIND OUR DUCTLESS SERVICES</h2>
<div class="promise" style="left:89px">
  <div class="photo" role="img" aria-label="Photo of a hand aiming a remote at a wall unit" style="background:linear-gradient(180deg,#f1f2f3,#2b4a80)"></div>
  <h3>GET SOME ANSWERS</h3><div class="btn btn-yellow">Ductless FAQ</div>
</div>
<div class="promise" style="left:438px">
  <div class="photo" role="img" aria-label="Photo of cash being handed across a desk" style="background:linear-gradient(180deg,#3a3f4a,#6b4a2c)"></div>
  <h3>OUR FINANCING OPTIONS</h3><div class="btn btn-yellow">Financing</div>
</div>
<div class="promise" style="left:785px">
  <div class="photo" role="img" aria-label="Photo of a remote control in front of an air unit" style="background:linear-gradient(180deg,#eceeef,#b07a55)"></div>
  <h3>STAY UP TO DATE</h3><div class="btn btn-yellow">Our blog</div>
</div>

<!-- footer -->
<svg class="abs" style="left:0;top:3783px" width="1200" height="520"><polygon points="0,0 1200,160 1200,520 0,520" fill="#000"/></svg>
<div class="brand" style="left:89px;top:4062px;color:var(--yellow);font-size:20px"><span class="dot"></span>Amber Kite Services</div>
<div class="footer-head" style="left:381px">Quick links</div>
<ul class="footer-list" style="left:381px;top:4006px"><li>Home</li><li>About Us</li><li>Ductless Heat Pumps</li><li>Ductless Heat Pumps FAQ</li><li>Financing</li><li>Contact Us</li></ul>
<div class="footer-head" style="left:595px">Contact info</div>
<div class="footer-contact" style="left:618px;top:4003px">Email:<br>info@example.com</div>
<div class="footer-contact" style="left:618px;top:4064px">Phone:<br>123-456-7890</div>
<div class="footer-contact" style="left:618px;top:4127px">Office Location:<br>Some address line goes here</div>
<svg class="abs" style="left:595px;top:4008px" width="14" height="150" viewBox="0 0 14 150" fill="#ffcc00"><rect x="1" y="2" width="12" height="9" rx="1"/><path d="M3 62a8 8 0 0 0 5 5l2-2 3 1v3a1 1 0 0 1-1 1A11 11 0 0 1 1 59a1 1 0 0 1 1-1h3l1 3z"/><path d="M7 118a5 5 0 0 1 5 5c0 4-5 9-5 9s-5-5-5-9a5 5 0 0 1 5-5z"/></svg>
<div class="footer-head" style="left:852px;top:3964px">Newsletter</div>
<div class="footer-contact" style="left:852px;top:4003px;font-size:12.5px;line-height:20px">Subscribe to our email address to<br>get the latest news.</div>
<div class="abs" style="left:852px;top:4063px;width:258px;height:40px;border-radius:20px;background:var(--white);font-size:12px;color:#666;display:flex;align-items:center;padding-left:36px">Enter Your Email...</div>
<div class="abs" style="left:1068px;top:4063px;width:42px;height:40px;border-radius:0 20px 20px 0;background:var(--yellow);display:flex;align-items:center;justify-content:center"><svg width="16" height="16" viewBox="0 0 16 16"><polygon points="1,7 15,1 10,15 8,9" fill="#111"/></svg></div>
<div class="social" style="left:853px;top:4126px;background:#3b5998"></div>
<div class="social" style="left:895px;top:4126px;background:#1da1f2"></div>
<div class="social" style="left:937px;top:4126px;background:#e00"></div>
<div class="social" style="left:979px;top:4126px;background:#b53ba0"></div>
<div class="abs" style="left:89px;top:4238px;width:1021px;height:1px;background:#222"></div>
<div class="abs" style="left:1136px;top:4215px;width:34px;height:34px;border-radius:50%;background:var(--white);display:flex;align-items:center;justify-content:center;font-size:14px">↑</div>
<div class="abs copyright">© Copyright 2019 &nbsp;|&nbsp; All Rights Reserved</div>

</body>
</html>
```